Brell Harbor Company Business Cards

Front and Back Business Card - logo and text setup - cool design. I need workable photoshop or illustrator files so I can setup each employee card with design that is created
Updates

Hi everyone, thank you for the great entries. Please no more white and blue cards - there are so many already - black and silver only now please. thanks!

Target Market(s)

Construction Industry - Facility Managers

Industry/Entity Type

Construction

Contact Information for Business Card

I really like contemporary simplistic looks - clean neat....not opposed to seeing some black backrounds

Requirements
Must have
• Logo/website address with design on front only - www.brellharbor-example.com (logo attached)
• Back:
• Name/Title/Company Address/Phone/email address
Nice to have
• Cool design
Should not have
• Nothing gimmicky like Fire or Water - since we are a Fire Protection company - it has all been done

```html
<!DOCTYPE html>
<html lang="en">
<head>
<meta charset="utf-8">
<title>Brell Harbor Company – Business Cards</title>
<link rel="stylesheet" href="https://fonts.googleapis.com/css2?family=Source+Sans+3:wght@400;600;700&display=swap">
<style>
  :root{
    --backdrop:#c9d4d4;
    --card-dark:#2f3438;
    --card-grey:#a5b1b4;
    --pill:#d5dfdf;
    --silver-light:#e4e8ea;
    --silver-mid:#b9c1c4;
    --silver-dark:#8c9599;
    --ink:#111416;
    --text-light:#eef1f2;
    --brand:#1f3f96;
    --icon:#2e86e6;
  }
  *{margin:0;padding:0;box-sizing:border-box}
  html,body{width:1200px;height:1000px;overflow:hidden}
  body{background:var(--backdrop);font-family:"Source Sans 3",Arial,sans-serif;position:relative}

  .card{position:absolute;width:600px;height:340px;left:300px;overflow:hidden;
        box-shadow:0 6px 14px rgba(0,0,0,.28)}
  .card--front{top:90px;background:var(--card-dark)}
  .card--back{top:540px;background:var(--card-dark)}

  /* front */
  .front-seal{position:absolute;left:50px;top:70px;width:200px;height:200px;border-radius:50%;
        background:radial-gradient(circle at 35% 30%,var(--silver-light),var(--silver-mid) 60%,var(--silver-dark));
        box-shadow:inset 0 0 0 2px rgba(255,255,255,.35);display:flex;align-items:center;justify-content:center}
  .brand-name{font-weight:700;color:var(--brand);font-size:24px;letter-spacing:.2px;white-space:nowrap}
  .front-url{position:absolute;left:285px;top:152px;color:var(--text-light);font-size:27px;font-weight:400;letter-spacing:.3px}

  /* back */
  .back-shapes{position:absolute;inset:0}
  .back-brand{position:absolute;left:345px;top:42px;width:255px;height:64px;display:flex;align-items:center;justify-content:center}
  .person{position:absolute;left:40px;top:44px;color:var(--ink)}
  .person-name{font-weight:700;font-size:24px;line-height:1.1}
  .person-title{font-size:22px;line-height:1.2}
  .contacts{position:absolute;left:28px;top:134px;list-style:none}
  .contact{display:flex;align-items:center;height:34px;margin-bottom:10px}
  .contact-icon{width:30px;height:30px;border-radius:9px;background:var(--icon);display:flex;align-items:center;justify-content:center;margin-right:12px}
  .contact-text{height:34px;line-height:34px;padding:0 20px;background:var(--pill);border-radius:0 8px 8px 8px;
        font-size:21px;color:var(--ink);border-left:4px solid var(--icon)}
  .contact:nth-child(1) .contact-text{width:300px}
  .contact:nth-child(2) .contact-text{width:330px}
  .contact:nth-child(3) .contact-text{width:355px}
  .contact:nth-child(4) .contact-text{width:380px}
</style>
</head>
<body>

<section class="card card--front" aria-label="Business card front">
  <div class="front-seal"><span class="brand-name">Brell Harbor</span></div>
  <p class="front-url">www.brellharbor-example.com</p>
</section>

<section class="card card--back" aria-label="Business card back">
  <svg class="back-shapes" width="600" height="340" viewBox="0 0 600 340">
    <defs>
      <linearGradient id="band-sheen" x1="0" y1="0" x2="1" y2="0">
        <stop offset="0" stop-color="#3a4044"/>
        <stop offset=".25" stop-color="#c9d0d3"/>
        <stop offset=".7" stop-color="#eef1f2"/>
        <stop offset="1" stop-color="#a9b2b5"/>
      </linearGradient>
    </defs>
    <rect class="brand-band" x="330" y="42" width="270" height="64" fill="url(#band-sheen)"/>
    <path class="info-panel" d="M0 0 H300 Q 500 110 540 340 H0 Z" fill="var(--card-grey)"/>
  </svg>

  <div class="back-brand"><span class="brand-name">Brell Harbor</span></div>

  <div class="person">
    <p class="person-name">Personal Name</p>
    <p class="person-title">Title</p>
  </div>

  <ul class="contacts">
    <li class="contact">
      <span class="contact-icon"><svg width="16" height="16" viewBox="0 0 24 24"><path d="M6.6 10.8a15 15 0 0 0 6.6 6.6l2.2-2.2c.3-.3.7-.4 1-.2 1.1.4 2.3.6 3.6.6.6 0 1 .4 1 1V20c0 .6-.4 1-1 1A17 17 0 0 1 3 4c0-.6.4-1 1-1h3.5c.6 0 1 .4 1 1 0 1.3.2 2.5.6 3.6.1.3 0 .7-.2 1z" fill="#fff"/></svg></span>
      <span class="contact-text">0123456789</span>
    </li>
    <li class="contact">
      <span class="contact-icon"><svg width="16" height="16" viewBox="0 0 24 24"><rect x="2" y="5" width="20" height="14" rx="2" fill="#fff"/><path d="M3 6l9 7 9-7" stroke="var(--icon)" stroke-width="2" fill="none"/></svg></span>
      <span class="contact-text">Email address</span>
    </li>
    <li class="contact">
      <span class="contact-icon"><svg width="16" height="16" viewBox="0 0 24 24" fill="none" stroke="#fff" stroke-width="2"><circle cx="12" cy="12" r="9"/><path d="M3 12h18M12 3c3 3 3 15 0 18M12 3c-3 3-3 15 0 18"/></svg></span>
      <span class="contact-text">www.brellharbor-example.com</span>
    </li>
    <li class="contact">
      <span class="contact-icon"><svg width="16" height="16" viewBox="0 0 24 24"><path d="M12 2a7 7 0 0 0-7 7c0 5 7 13 7 13s7-8 7-13a7 7 0 0 0-7-7z" fill="#fff"/><circle cx="12" cy="9" r="2.5" fill="var(--icon)"/></svg></span>
      <span class="contact-text">Company Address</span>
    </li>
  </ul>
</section>

</body>
</html>
```